Resume for higher management position in a mechanical/consultant industries application*

I would like to use this resume for getting a higher position interview possibilities. My skills are multi-cultural negotiation, mechanical industry sales, outsourcing to Asia, ability to manage the agent/reseller system, well team player. multi-language Chinese/English/German specialized. Please make the design, professional, comfortable to read atmosphere.

Target Market(s)

management position, sales related

Font styles to use
Serif
Sans Serif

```html
<!DOCTYPE html>
<html lang="en">
<head>
<meta charset="utf-8">
<title>Ming-Hao Lin – Resume</title>
<link rel="stylesheet" href="https://fonts.googleapis.com/css2?family=Lato:wght@400;700;900&display=swap">
<style>
  :root{
    --ink:#3b3b3d;
    --text:#333333;
    --panel:#efefef;
    --bar-track:#e6e6e6;
    --accent:#d0021b;
    --paper:#ffffff;
  }
  *{margin:0;padding:0;box-sizing:border-box}
  html,body{width:1200px;height:802px;overflow:hidden;background:var(--paper)}
  body{font-family:"Lato",Arial,sans-serif;color:var(--text);position:relative}
  .abs{position:absolute}

  .panel{position:absolute;background:var(--panel)}
  .panel--left{left:13px;top:14px;width:267px;height:755px}
  .panel--skills{left:593px;top:20px;width:264px;height:742px}

  .name-bar{left:38px;top:14px;width:14px;height:68px;background:var(--ink)}
  .name{left:60px;top:38px;font-size:25px;font-weight:700;color:var(--ink);letter-spacing:-.3px}
  .role{left:60px;top:67px;font-size:13px;letter-spacing:3px;color:var(--ink)}

  .heading{position:absolute;font-weight:700;color:var(--ink);display:flex;align-items:flex-start;gap:10px}
  .heading::before{content:"";width:14px;height:14px;background:var(--ink);flex:none;margin-top:2px}
  .heading--caps{font-size:14px;letter-spacing:3px;text-transform:uppercase}
  .heading--plain{font-size:13.5px}
  .heading--tall::before{width:14px;height:34px;margin-top:0}

  .info{left:60px;top:126px;font-size:11px;line-height:16.2px}
  .info b{font-weight:700}
  .summary{left:61px;top:258px;width:213px;font-size:10.8px;line-height:16.2px}
  .summary p+p{margin-top:16px}

  .edu{left:315px;top:70px;width:230px;font-size:12.8px;line-height:19.6px;letter-spacing:.6px}
  .edu p+p{margin-top:20px}
  .specialties{left:319px;top:281px;width:210px;font-size:11.2px;line-height:18px;letter-spacing:.2px}

  .qualities{left:312px;top:422px}
  .qualities text{font-family:"Lato",Arial,sans-serif;font-size:9px;fill:var(--text)}

  .meter-label{position:absolute;font-size:9.4px;color:var(--text)}
  .meter{position:absolute;height:8px;background:var(--bar-track)}
  .meter span{display:block;height:100%;background:var(--ink)}

  .photo{left:643px;top:20px;width:179px;height:298px;background:var(--ink)}

  .links{left:664px;top:638px;font-size:9.2px;line-height:20.5px}
  .links li{list-style:none;display:flex;align-items:center;gap:10px}
  .links li::before{content:"";width:15px;height:15px;border-radius:50%;background:var(--ink);flex:none}

  .job{position:absolute;font-size:9.2px;line-height:16px;width:230px}
  .job .date{color:var(--accent);font-size:11px;font-weight:700;margin-bottom:3px}
  .job .title{font-weight:700;font-size:9.4px}
  .job p{margin-top:3px}
  .job p+p{margin-top:14px}
</style>
</head>
<body>

<div class="panel panel--left"></div>
<div class="panel panel--skills"></div>

<!-- Identity -->
<div class="abs name-bar"></div>
<div class="abs name">Ming-Hao Lin</div>
<div class="abs role">ARCHITECTURE</div>

<div class="heading heading--plain" style="left:39px;top:105px">Personal Information</div>
<div class="abs info">
  <div><b>Name:</b> Ming-Hao Lin</div>
  <div><b>Date &amp; Place of birth:</b> xxxxxxx</div>
  <div><b>Nationality:</b> Taiwanese</div>
  <div><b>Address:</b> xxxxxxxx, Germany</div>
  <div><b>Mobile:</b> +xxxxxx</div>
  <div><b>Email:</b> xxxxxx@postmail.com</div>
</div>

<div class="heading heading--plain" style="left:39px;top:237px">Summary:</div>
<div class="abs summary">
  <p>Mandarin Chinese/German/English speaker, real machining experience, OEM skills, trade skill, global sourcing. Currently I am "Sales manager Asia" of a top German rotary table company. I am in charge of four countries Japan, China, South Korea and Taiwan with 3 agents, more than 20 salesmen. As a director of manufacturing, I have more than 5 years professional experience in manufacturing metal components by different CNC machines. I am capable of coding CNC G, M-code, designing the working path of different parts and managing the whole process.</p>
  <p>I have well understanding of mechanical outsourcing system in Taiwan. With deep knowledge of outsourcing metal components to different suppliers in Taiwan.</p>
  <p>Familiar with coordinating with different industrial processes in order to build the final products. (Black oxidizing, Different anodizing, Chemical polishing, Manganese phosphate coating, Heat treatment, and Different grinding methods) Especially love to build prototypes in order to get a high profitable potential products. (from zero to one)</p>
</div>

<!-- Education & specialties -->
<div class="heading heading--caps" style="left:292px;top:47px">Education</div>
<div class="abs edu">
  <p>MBA degree from ASM,<br>Politecnico Valtellina.<br>MBA, Politecnico<br>Valtellina 2011-2012</p>
  <p>Bachelor of Chemical engineering,<br>Taoyuan Hill<br>University 2005-2009</p>
</div>

<div class="heading heading--plain" style="left:295px;top:263px">SPECIALTIES:</div>
<div class="abs specialties">Great experiences in handling business with Chinese-cultural business firms. Multi-national corporations skills (especially in Chinese-speaking market)</div>

<div class="heading heading--caps" style="left:292px;top:392px">Key Qualities</div>
<svg class="abs qualities" width="160" height="160" viewBox="0 0 160 160" aria-label="Key qualities">
  <g fill="none" stroke="var(--ink)" stroke-width="1">
    <circle cx="36" cy="35" r="33"/>
    <circle cx="113" cy="35" r="33"/>
    <circle cx="75" cy="78" r="33"/>
    <circle cx="36" cy="121" r="33"/>
    <circle cx="113" cy="121" r="33"/>
  </g>
  <g text-anchor="middle">
    <text x="36" y="38">Specialist</text>
    <text x="113" y="38">Innovative</text>
    <text x="75" y="81">Creative</text>
    <text x="36" y="124">Team Work</text>
    <text x="113" y="124">Dependable</text>
  </g>
</svg>

<div class="heading heading--caps" style="left:299px;top:605px">Languages</div>
<div class="meter-label" style="left:322px;top:632px">native Chinese speaker</div>
<div class="meter" style="left:322px;top:647px;width:193px"><span style="width:139px"></span></div>
<div class="meter-label" style="left:322px;top:669px">advanced English</div>
<div class="meter" style="left:322px;top:683px;width:193px"><span style="width:139px"></span></div>
<div class="meter-label" style="left:322px;top:705px">advanced German</div>
<div class="meter" style="left:322px;top:719px;width:193px"><span style="width:105px"></span></div>

<!-- Photo & skills -->
<div class="abs photo" role="img" aria-label="Portrait photo of the candidate"></div>

<div class="heading heading--caps heading--tall" style="left:641px;top:348px;line-height:20px">Softwares<br>Skills</div>
<div class="meter-label" style="left:664px;top:397px">Hand Drafting &amp; Model Making</div>
<div class="meter" style="left:664px;top:410px;width:169px"><span style="width:159px"></span></div>
<div class="meter-label" style="left:664px;top:430px">DraftCore</div>
<div class="meter" style="left:664px;top:443px;width:169px"><span style="width:159px"></span></div>
<div class="meter-label" style="left:664px;top:463px">Structa BIM</div>
<div class="meter" style="left:664px;top:476px;width:169px"><span style="width:159px"></span></div>
<div class="meter-label" style="left:664px;top:497px">FormSketch - Lumen</div>
<div class="meter" style="left:664px;top:510px;width:169px"><span style="width:159px"></span></div>
<div class="meter-label" style="left:664px;top:531px">PixelForge Studio</div>
<div class="meter" style="left:664px;top:544px;width:169px"><span style="width:139px"></span></div>
<div class="meter-label" style="left:664px;top:568px">Deskwork Suite</div>
<div class="meter" style="left:664px;top:581px;width:169px"><span style="width:159px"></span></div>

<div class="heading heading--caps" style="left:641px;top:613px">Links</div>
<ul class="abs links">
  <li>www.picfolio.com/Ming-HaoLin</li>
  <li>www.chirpline.com/Ming-HaoLin</li>
  <li>www.workmesh.com/Ming-HaoLin</li>
  <li>www.friendboard.com/Ming-HaoLin</li>
</ul>

<!-- Experience -->
<div class="heading heading--caps heading--tall" style="left:871px;top:52px;line-height:20px">Professional<br>Experience</div>

<div class="job" style="left:891px;top:98px">
  <div class="date">June 2018 - Now</div>
  <div class="title">Sales Manager Asia</div>
  <p>Currently, leading 3 major dealers in Taiwan, Mainland-China, South Korea and Japan with more than 20 sales-men team.</p>
  <p>Kesselmann provides rotary tables, trunnions and 2 axis-rotary tilt units shall have the best possible technical characteristics in the smallest possible space, is the principle model for our dividing heads-engineering-manufacturing-and assembly.</p>
</div>

<div class="job" style="left:893px;top:298px">
  <div class="date">March 2012 - December 2017</div>
  <div class="title">Director of Manufacturing,<br>Brandel Precision Machinery Company</div>
  <p>Using CNC turn/mill machine to manufacture any mechanical components as customers want. Also providing great total solutions for our clients.</p>
  <p>Photos shown in my profile are my products which are made by CNC turn-milling dual spindle machines (trophy is programmed by CAM).</p>
</div>

<div class="job" style="left:893px;top:484px">
  <div class="date">2012 Apr - 2012 Nov</div>
  <div class="title">Marketing Analyst, Greenfield Import<br>Mannheim Germany</div>
  <p>Help Greenfield Import to build their sales/marketing strategy for the new launched product "Glide-fix" in central Europe.</p>
</div>

<div class="job" style="left:897px;top:616px">
  <div class="date">2012 Apr - 2012 Nov</div>
  <div class="title">External consultant, Calcara<br>Group Bergamo Italy</div>
  <p>To improve the Vertex solution (ERP system) of Calcara with the re-organized procurement process and new standardized KPIs.</p>
</div>

</body>
</html>
```